Varnel Consulting needs a business card design

Varnel Consulting is a small business that consults and trains Australia wide in Workplace Health and Safety, Environment and Quality Management Systems.

Clients are typically smaller businesses with 50 to 200 employees but there are some large clients.

Communication is often by email, although mobile is used as well.

Varnel Consulting
61 Tormoth Vale Road
Pellowby, QLD 4391
0438 912 047

```html
<!DOCTYPE html>
<html lang="en">
<head>
<meta charset="utf-8">
<title>Varnel Consulting – Business Card</title>
<link href="https://fonts.googleapis.com/css2?family=Roboto:wght@700&family=Open+Sans:wght@400;600&display=swap" rel="stylesheet">
<style>
  :root {
    --backdrop: #1f1f20;
    --brand-blue: #2f5aa6;
    --brand-blue-deep: #1f3f86;
    --brand-blue-light: #3d6bbd;
    --card-light: #f1f1f2;
    --panel-grey: #e2e3e5;
    --charcoal: #575757;
    --text-grey: #5a5a5a;
    --white: #ffffff;
  }
  * { box-sizing: border-box; margin: 0; padding: 0; }
  html, body { width: 1200px; height: 1000px; overflow: hidden; }
  body { background: var(--backdrop); position: relative; font-family: "Open Sans", sans-serif; }

  .card {
    position: absolute;
    width: 560px;
    height: 340px;
    overflow: hidden;
    box-shadow: 0 14px 34px rgba(0,0,0,0.55);
  }

  /* Back of card */
  .card-back {
    left: 90px; top: 110px;
    background: linear-gradient(135deg, var(--brand-blue-light), var(--brand-blue-deep));
  }
  .card-back .back-disc {
    position: absolute;
    left: 120px; top: 40px;
    width: 320px; height: 320px;
    border-radius: 50%;
    background: var(--white);
  }
  .card-back .back-name {
    position: absolute;
    left: 0; right: 0; top: 150px;
    text-align: center;
    font-family: "Roboto", sans-serif;
    font-weight: 700;
    font-size: 34px;
    color: var(--brand-blue);
  }

  /* Front of card */
  .card-front {
    left: 550px; top: 520px;
    background: var(--card-light);
  }
  .front-band {
    position: absolute;
    left: 0; top: 0; bottom: 0;
    width: 200px;
    background: linear-gradient(160deg, var(--brand-blue-light), var(--brand-blue-deep));
  }
  .front-band-edge {
    position: absolute;
    left: 200px; top: 0; bottom: 0;
    width: 8px;
    background: var(--charcoal);
  }
  .front-panel {
    position: absolute;
    left: 222px; top: 12px; right: 12px; bottom: 52px;
    border-radius: 14px;
    background: linear-gradient(180deg, #ebecee, var(--panel-grey));
  }
  .front-disc {
    position: absolute;
    left: 30px; top: 34px;
    width: 272px; height: 272px;
    border-radius: 50%;
    background: var(--charcoal);
    border: 2px solid var(--white);
  }
  .company-name {
    position: absolute;
    right: 30px; top: 28px;
    text-align: right;
    font-family: "Roboto", sans-serif;
    font-weight: 700;
    font-size: 30px;
    line-height: 1.05;
    color: var(--brand-blue);
  }
  .contact-block {
    position: absolute;
    right: 30px; top: 178px;
    text-align: right;
    font-size: 12px;
    line-height: 1.6;
    color: var(--text-grey);
  }
  .contact-block .label { font-weight: 600; }
  .contact-email {
    position: absolute;
    right: 30px; bottom: 20px;
    font-size: 12px;
    color: var(--text-grey);
  }
  .contact-email .label { font-weight: 600; }
</style>
</head>
<body>

  <section class="card card-back" aria-label="Card back">
    <div class="back-disc"></div>
    <p class="back-name">Varnel Consulting</p>
  </section>

  <section class="card card-front" aria-label="Card front">
    <div class="front-band"></div>
    <div class="front-band-edge"></div>
    <div class="front-panel"></div>
    <div class="front-disc"></div>

    <h1 class="company-name">Varnel<br>Consulting</h1>

    <address class="contact-block" style="font-style:normal">
      61 Tormoth Vale Road<br>
      Pellowby, QLD 4391<br>
      <span class="label">tel:</span> 0438 912 047
    </address>

    <p class="contact-email"><span class="label">email:</span> info@varnelconsulting.net</p>
  </section>

</body>
</html>
```